Company Brochure / Sales Sheet

We would like a brochure that we will may print out as well as forward electronically to our prospective clients.

Our clients are inventors/doctors/surgeons of medical products who need help completing their medical product, gaining approval, and then selling their product into the US market

Target Market(s)

Inventors of medical products who want to sell them in the United States

Industry/Entity Type

Medical

Font styles to use
Serif
Sans Serif

Requirements
Must have
• The word "Medical" should not receive special empahsis.
• Use the last two photos and whatever other photos that look good. You can edit and crop the photos
• Text should be easy to read
Nice to have
• We want to show that we have a lot of products.
• Sharp, clean, modern
• Minimum two pages - final product should be capable of being printed and
• forwarded electronically
• Easy to read
Should not have
• Should not be cluttered

```html
<!DOCTYPE html>
<html lang="en">
<head>
<meta charset="utf-8">
<title>Carewell Distribution Network – Brochure</title>
<link href="https://fonts.googleapis.com/css2?family=Montserrat:wght@600;700&family=Arimo:wght@400;700&display=swap" rel="stylesheet">
<style>
  :root{
    --stage:#1e1e1e;
    --paper:#ffffff;
    --red:#c8202f;
    --red-deep:#b01c2a;
    --orange:#f7a13c;
    --purple:#5b1a8c;
    --ink:#1a1a1a;
    --sky:#2f8fc4;
    --sky-deep:#0f4f86;
  }
  *{box-sizing:border-box;margin:0;padding:0}
  html,body{width:1200px;height:1200px;overflow:hidden;background:var(--stage)}
  body{position:relative;font-family:"Arimo",Arial,sans-serif;color:var(--ink)}
  .page{position:absolute;background:var(--paper);overflow:hidden}
  .page--back{left:156px;top:41px;width:423px;height:548px}
  .page--cover{left:598px;top:41px;width:424px;height:548px;background:linear-gradient(#fff 55%,#fdeeea)}
  .page--about{left:158px;top:609px;width:424px;height:546px;background:linear-gradient(160deg,#f4f7fa 30%,#dce8f2 70%,#9fb9d4)}
  .page--services{left:598px;top:609px;width:424px;height:549px}

  .brand{position:absolute;left:0;right:0;text-align:center}
  .brand__dot{display:block;width:24px;height:24px;border-radius:50%;background:var(--red);margin:0 auto 6px}
  .brand__name{font-family:"Montserrat",sans-serif;font-weight:700;font-size:9.5px;letter-spacing:.3px;color:var(--ink);line-height:1.3}

  .contact{position:absolute;left:0;right:0;top:263px;text-align:center;font-size:11.5px;line-height:13px}
  .wave{position:absolute;left:0;width:100%}

  .tagline{position:absolute;left:0;right:0;top:306px;text-align:center;color:var(--purple);font-size:14.5px}
  .cover-footer{position:absolute;left:0;right:0;bottom:0;height:53px;background:var(--red);color:#fff;font-size:9.5px;display:flex;justify-content:center;align-items:center;gap:15px;padding-left:20px}

  .about-panel{position:absolute;left:6px;top:18px;width:409px;height:397px;background:rgba(200,32,47,.93);border-radius:6px;color:#fff}
  .about-panel h2{font-family:"Montserrat",sans-serif;font-size:13.5px;font-weight:700;position:absolute;left:8px;top:6px}
  .photo{display:block}
  .about-panel .photo{position:absolute;left:8px;top:40px;width:392px;height:153px;background:linear-gradient(#fff,#e9eef2 60%,#cfd8e0)}
  .about-copy{position:absolute;left:8px;top:205px;width:393px;font-size:7.6px;line-height:10px;text-align:justify}
  .about-copy p+p{margin-top:10px}
  .tool-tile{position:absolute;top:439px;width:120px;height:85px;background:#fff;border-radius:6px;padding:10px}
  .tool-tile .photo{width:100%;height:100%;background:linear-gradient(#fff,#e8e8e8 50%,#fff)}

  .stripe{position:absolute;left:0;width:100%}
  .services-photo{position:absolute;left:15px;top:26px;width:147px;height:196px;border-radius:8px;background:linear-gradient(135deg,#9fc6d6,#5e8ea3 45%,#2e3d44)}
  .services-copy{position:absolute;left:172px;top:26px;width:234px;font-size:6.4px;line-height:8.2px;text-align:justify}
  .services-copy h3{font-family:"Montserrat",sans-serif;color:var(--red);font-size:7px;font-weight:700;margin-bottom:9px}
  .services-copy p{margin-bottom:8px}
  .services-copy p+h3{margin-top:2px}
  .products-tag{position:absolute;left:306px;top:240px;width:118px;height:26px;background:var(--red);color:#fff;font-size:13px;display:flex;align-items:center;justify-content:center}
  .product{position:absolute;width:92px}
  .product .photo{height:90px;border-radius:3px;border:2px solid #1f3146;background:linear-gradient(#fafafa,#cfd3d6)}
  .product--cobb .photo{border:none;background:linear-gradient(135deg,#5f9ff0,#1b4fbf)}
  .product figcaption{font-family:"Montserrat",sans-serif;font-weight:700;font-size:8px;margin-top:5px;line-height:9.5px}
  .corner{position:absolute;right:0;bottom:0}
</style>
</head>
<body>

<!-- Back page -->
<section class="page page--back">
  <div class="brand" style="top:195px">
    <span class="brand__dot"></span>
    <div class="brand__name">CAREWELL DISTRIBUTION NETWORK</div>
  </div>
  <div class="contact">
    <p>Phone:&nbsp; (555) 014-2290</p>
    <p>Website:&nbsp; www.carewelldistribution.com</p>
  </div>
  <svg class="wave" style="top:405px" width="423" height="110" viewBox="0 0 423 110">
    <path d="M0 5 C80 60 160 85 250 55 C320 30 380 15 423 20 L423 24 C370 22 320 40 250 70 C160 105 80 95 0 45Z" fill="var(--orange)" opacity=".45"/>
    <path d="M0 18 C80 70 160 90 250 60 C320 35 380 20 423 24 L423 30 C370 30 320 48 250 78 C160 112 80 100 0 58Z" fill="var(--orange)"/>
    <path d="M0 32 C80 85 160 102 250 72 C320 48 380 32 423 30 L423 36 C370 40 320 62 250 88 C150 124 70 112 0 80Z" fill="var(--red)"/>
  </svg>
</section>

<!-- Cover -->
<section class="page page--cover">
  <svg class="wave" style="top:0" width="424" height="215" viewBox="0 0 424 215">
    <defs>
      <linearGradient id="heroSky" x1="0" y1="0" x2="1" y2="1">
        <stop offset="0" stop-color="#7fc0e4"/><stop offset=".5" stop-color="var(--sky)"/><stop offset="1" stop-color="var(--sky-deep)"/>
      </linearGradient>
    </defs>
    <rect width="424" height="215" fill="url(#heroSky)" role="img" aria-label="Photo of a smiling lab scientist in safety glasses before a digital interface"/>
    <path d="M0 135 C90 150 170 210 270 205 C340 200 390 175 424 150 L424 215 L0 215Z" fill="#fff"/>
    <path d="M0 132 C90 138 170 190 270 188 C340 186 390 165 424 138 L424 150 C390 178 340 200 270 205 C170 210 90 150 0 140Z" fill="var(--red)"/>
    <path d="M0 128 C90 132 170 180 270 178 C340 176 390 155 424 130 L424 138 C390 165 340 186 270 188 C170 190 90 138 0 132Z" fill="var(--orange)"/>
  </svg>
  <div class="brand" style="top:238px">
    <span class="brand__dot"></span>
    <div class="brand__name">CAREWELL DISTRIBUTION NETWORK</div>
  </div>
  <h1 class="tagline">Saving Lives &amp; Reducing Health Care Costs</h1>
  <nav class="cover-footer"><span>Medical Products</span><span>Regulatory Issues</span><span>Intellectual Property and Branding</span></nav>
</section>

<!-- About us -->
<section class="page page--about">
  <div class="about-panel">
    <h2>ABOUT US</h2>
    <span class="photo" role="img" aria-label="Photo of a team of smiling doctors in white coats with stethoscopes"></span>
    <div class="about-copy">
      <p>We are a network of medical distribution professionals including physicians and surgeons, regulatory and coding experts, patent and trademark lawyers, international fulfillment experts, marketing and advertising professionals, and business strategists all working together in the distribution of promising new medical products. We handle all aspects of new surgical product sales, marketing, and distribution.</p>
      <p>Our company was founded in Brookhaven, Maine, with distribution locations and support associates and affiliates located throughout the US. We have extensive experience with medical product development, intellectual property, and regulatory and compliances issues.</p>
      <p>We partner with medical innovators by providing strategic support with intellectual property and regulatory approval, reimbursement coding, marketing, selling and distributing state of the art medical products. Our clients include highly creative medical companies with strong management teams and consumer-driven growth perspectives.</p>
      <p>Our products are uniquely positioned in an evolving health sector to offer benefits to patients, healthcare institutions, medical professionals, insurance companies and governmental agencies. Our evidence-based technologies reduce overall healthcare expenses and empower physicians and surgeons to provide improved practices and standards of care.</p>
    </div>
  </div>
  <div class="tool-tile" style="left:14px"><span class="photo" role="img" aria-label="Photo of a surgical rongeur"></span></div>
  <div class="tool-tile" style="left:150px"><span class="photo" role="img" aria-label="Photo of a Kerrison punch instrument"></span></div>
  <div class="tool-tile" style="left:286px"><span class="photo" role="img" aria-label="Photo of a surgical forceps"></span></div>
</section>

<!-- Services and products -->
<section class="page page--services">
  <svg class="stripe" style="top:2px" width="424" height="13" viewBox="0 0 424 13">
    <rect y="0" width="424" height="4" fill="var(--red)"/>
    <rect y="4" width="424" height="5" fill="var(--orange)"/>
    <rect y="9" width="424" height="4" fill="var(--red)"/>
  </svg>
  <span class="services-photo" role="img" aria-label="Photo of a businessman working with a holographic data display"></span>
  <div class="services-copy">
    <h3>Medical Products</h3>
    <p>We specialize in the distribution of next generation medical products including customized surgical instruments and kits, monitoring and diagnostic devices, advanced wound care products and innovative acute care disposables</p>
    <p>Our medical products represent breakthroughs in medical technology, saving lives, reducing health care costs, improving patient lifestyles.</p>
    <h3>Intellectual Property and Branding</h3>
    <p>We help our partners get the trademarks and patent claim approvals they need and deserve and at a reasonable price. Our team of patent attorneys and agents is effective and affordable and has gained over 300 client patent approvals. We help our clients brand and position their products for successful product launches and introductions to the US market.</p>
    <h3>Regulatory Issues</h3>
    <p>We provide comprehensive services support for global physician inventors who are seeking to distribute their medical products within the United States. We assist in navigating the unique aspects of the US medical market – including FDA compliance and device returns, US Customs, and reimbursement coding.</p>
  </div>
  <div class="products-tag">OUR PRODUCTS</div>
  <figure class="product" style="left:15px;top:277px"><span class="photo" role="img" aria-label="Photo of a needle holder"></span></figure>
  <figure class="product" style="left:152px;top:277px"><span class="photo" role="img" aria-label="Photo of surgical scissors"></span><figcaption>Scissors</figcaption></figure>
  <figure class="product" style="left:289px;top:277px"><span class="photo" role="img" aria-label="Photo of a surgical clamp"></span><figcaption>Clamps</figcaption></figure>
  <figure class="product" style="left:15px;top:400px"><span class="photo" role="img" aria-label="Photo of a minimally invasive instrument"></span><figcaption>Minimally Invasive</figcaption></figure>
  <figure class="product" style="left:152px;top:400px"><span class="photo" role="img" aria-label="Photo of an orthopedic cutter"></span><figcaption>Orthopedic</figcaption></figure>
  <figure class="product product--cobb" style="left:289px;top:400px"><span class="photo" role="img" aria-label="Photo of a yellow combination cobb elevator"></span><figcaption>Combination cob elevator and suction device</figcaption></figure>
  <svg class="corner" width="56" height="56" viewBox="0 0 56 56">
    <path d="M56 0 L56 56 L0 56Z" fill="var(--orange)"/>
    <path d="M56 28 L56 56 L28 56Z" fill="var(--red)"/>
  </svg>
</section>

</body>
</html>
```